Brenvik Auto Logo Design

Brenvik Auto Sales & Service is a automotive repair shop and car dealership. We specialize in Norvane & Kestrelwerk, so we would like our cards to let our customers know that we are a German import specialist and that we are QTR certified. We are looking for something that is sharp, with clean lines, and very professional. We specialize in Norvane and Kestrelwerk, so we want to appeal to the higher end customer. We want a business card that will do so. Please no cars, tires or tools on the logo. We want this to look tactful and professional. We would also like our link to our facebook page included on the business card. https://www.examplesocial.test/brenvikautosalesservice

Industry/Entity Type

Automotive

Contact Information for Business Card

Brenvik Auto Sales & Service
Doug & Melinda Brenvik
482 E Thornbury Avenue
PO Box 63
Ashgrove, MN 54911
Phone 715-555-0187
Fax 715-555-0193

Logo Text

```html
<!DOCTYPE html>
<html lang="en">
<head>
<meta charset="utf-8">
<title>Brenvik Auto Sales &amp; Service – Business Card</title>
<link rel="stylesheet" href="https://fonts.googleapis.com/css2?family=Lato:wght@400;700&display=swap">
<style>
  :root {
    --backdrop: #5b5b5b;
    --card: #0f0f0f;
    --gold: #c48c2f;
    --ink: #f2f2f2;
  }
  * { margin: 0; padding: 0; box-sizing: border-box; }
  html, body { width: 1200px; height: 1000px; overflow: hidden; }
  body {
    position: relative;
    background: var(--backdrop);
    font-family: "Lato", sans-serif;
  }
  .card {
    position: absolute;
    top: 169px;
    width: 388px;
    height: 662px;
    background: var(--card);
  }
  .card--back { left: 175px; }
  .card--front { left: 625px; }

  .brand {
    position: absolute;
    right: 63px;
    top: 102px;
    text-align: right;
    color: var(--gold);
  }
  .brand__name {
    font-weight: 700;
    font-size: 62px;
    line-height: 1;
    letter-spacing: 1px;
  }
  .brand__tagline {
    margin-top: 10px;
    color: var(--ink);
    font-size: 17px;
    letter-spacing: 1.6px;
  }

  .owners {
    position: absolute;
    left: 65px;
    top: 268px;
    color: var(--gold);
    font-weight: 700;
    font-size: 29px;
    line-height: 31px;
  }

  .contact {
    position: absolute;
    left: 65px;
    top: 382px;
    list-style: none;
  }
  .contact__item {
    display: flex;
    align-items: center;
    height: 28px;
    color: var(--ink);
    font-size: 18px;
  }
  .contact__icon {
    width: 20px;
    height: 20px;
    margin-right: 16px;
    flex: none;
  }

  .address {
    position: absolute;
    left: 65px;
    top: 502px;
    color: var(--ink);
    font-size: 18px;
    line-height: 28px;
    font-style: normal;
  }
  .address__company {
    color: var(--gold);
    font-weight: 700;
    font-size: 17px;
  }
</style>
</head>
<body>
  <div class="card card--back" aria-label="Card back"></div>

  <div class="card card--front">
    <div class="brand">
      <div class="brand__name">Brenvik</div>
      <div class="brand__tagline">AUTO SALES &amp; SERVICE</div>
    </div>

    <div class="owners">Doug &amp; Melinda<br>Brenvik</div>

    <ul class="contact">
      <li class="contact__item">
        <svg class="contact__icon" viewBox="0 0 20 20" aria-hidden="true">
          <rect width="20" height="20" rx="3" fill="var(--gold)"/>
          <path d="M6 4c1 0 2 2.5 2 3s-1.2 1-1 1.6c.6 1.6 2 3 3.6 3.6.6.2 1-1 1.6-1s3 1 3 2-1 2.5-2.5 2.5C8 15.7 4.3 12 4.3 7.5 4.3 5 5 4 6 4z" fill="var(--card)"/>
        </svg>
        715-555-0187
      </li>
      <li class="contact__item">
        <svg class="contact__icon" viewBox="0 0 20 20" aria-hidden="true">
          <rect width="20" height="20" rx="3" fill="var(--gold)"/>
          <rect x="6" y="3.5" width="8" height="4" fill="var(--card)"/>
          <rect x="3.5" y="8" width="13" height="6" rx="1" fill="var(--card)"/>
          <rect x="6" y="12" width="8" height="4.5" fill="var(--card)" stroke="var(--gold)" stroke-width="1"/>
        </svg>
        715-555-0193
      </li>
      <li class="contact__item">
        <svg class="contact__icon" viewBox="0 0 20 20" aria-hidden="true">
          <rect width="20" height="20" rx="3" fill="var(--gold)"/>
        </svg>
        brenvikautosalesservice
      </li>
    </ul>

    <address class="address">
      <div class="address__company">Brenvik Auto Sales &amp; Service</div>
      <div>482 E Thornbury Avenue</div>
      <div>P.O. Box 63 Ashgrove, MN 54911</div>
    </address>
  </div>
</body>
</html>
```